Landing Page Side by Side With Dr. Korwell

Hello!

I am looking for a high converting Landing Page for a One on One Coaching program that Dr. Korwell is releasing. I created a moch up for content but the spacing and graphics are not cohesive. I like the medical look at the top of the first page - the image is the graphic "Get Side BY Side Support from Dr. Korwell.
Please let me know if you have any questions!
Thank you!

```html
<!DOCTYPE html>
<html lang="en">
<head>
<meta charset="utf-8">
<title>Side by Side With Dr. Korwell – Landing Page</title>
<link rel="stylesheet" href="https://fonts.googleapis.com/css2?family=Arimo:wght@400;700&family=Open+Sans:wght@400;600&family=Oswald:wght@500;600&display=swap">
<style>
  :root{
    --brand-blue:#0f3b93;
    --nav-blue:#1643a3;
    --deep-blue:#0b2f7a;
    --orange:#ef8a1f;
    --ink:#141414;
    --muted:#6b6b6b;
    --band-grey:#eeeeee;
    --line-grey:#c9c9c9;
    --backdrop:#e8eaed;
    --white:#ffffff;
  }
  *{box-sizing:border-box;margin:0;padding:0}
  html,body{width:1200px;height:1200px;overflow:hidden}
  body{background:var(--backdrop);font-family:"Arimo",Arial,sans-serif;color:var(--ink);position:relative}

  .page{position:absolute;left:397px;top:20px;width:406px;height:1160px;background:var(--white);overflow:hidden}
  .page > *{position:absolute}

  /* header */
  .brand{left:31px;top:16px;display:flex;align-items:center;gap:5px}
  .brand__name{font-family:"Oswald",sans-serif;font-weight:600;font-size:21px;line-height:20px;color:var(--brand-blue);width:70px;text-transform:uppercase}
  .brand__dot{width:12px;height:12px;border-radius:50%;background:var(--brand-blue)}
  .contact-lines{left:306px;top:45px;font-size:8.5px;line-height:10px;color:var(--brand-blue);font-weight:700}
  .contact-lines span{display:inline-block;width:28px}

  .nav{left:0;top:72px;width:406px;height:21px;background:var(--nav-blue)}
  .nav a{position:absolute;top:4px;font-size:9px;color:var(--white);text-decoration:none;line-height:13px}
  .nav a.is-active{background:#8a8f99;padding:0 5px;border-radius:2px;left:193px}

  /* hero */
  .hero{left:0;top:97px;width:406px;height:156px;background:linear-gradient(180deg,#dfe3e9 0%,#c9d0da 22%,#2450a8 40%,#1b45a0 78%,#ffffff 78.5%,#ffffff 100%)}
  .hero__photo{position:absolute;left:25px;top:0;width:118px;height:156px;background:linear-gradient(180deg,#cdd2da 0%,#e9ebee 55%,#f4f4f4 100%)}
  .hero__title{position:absolute;left:138px;top:44px;width:240px;text-align:center;color:var(--white);font-family:"Open Sans",sans-serif}
  .hero__title h1{font-weight:400;font-size:18.5px;line-height:22px}
  .hero__title p{font-size:11.5px;line-height:15px}
  .hero__dots{position:absolute;left:375px;top:112px;display:flex;gap:3px}
  .hero__dots i{width:4px;height:4px;border-radius:50%;background:var(--white)}
  .hero__name{position:absolute;right:14px;top:129px;font-family:"Oswald",sans-serif;font-weight:500;font-size:14px;color:var(--brand-blue);text-transform:uppercase}

  /* intro */
  .headline{left:0;top:268px;width:406px;text-align:center;font-weight:700;font-size:16px}
  .intro{left:44px;top:302px;width:196px;text-align:center;font-size:10px;line-height:12.5px}
  .video{left:256px;top:292px;width:117px;height:81px;background:linear-gradient(160deg,#4a4f58,#2b2f36)}
  .video__play{position:absolute;left:46px;top:28px}

  .brand--center{left:0;top:393px;width:406px;justify-content:center}
  .brand--center .brand__name{width:auto;text-align:center}

  .commit{left:0;top:452px;width:406px;text-align:center;font-family:"Oswald",sans-serif;font-weight:600;font-size:14px;color:var(--brand-blue);text-transform:uppercase}
  .goals{left:69px;top:470px;width:300px;display:grid;grid-template-columns:159px 1fr;row-gap:3px;list-style:none}
  .goals li{font-size:9.5px;line-height:12px;color:var(--brand-blue);display:flex;align-items:center;gap:5px}
  .goals li::before{content:"";width:6px;height:6px;border-radius:50%;background:var(--orange)}

  .btn{display:block;text-align:center;color:var(--white);font-family:"Arimo",sans-serif;text-decoration:none}
  .btn--blue{left:60px;top:537px;width:287px;height:26px;line-height:26px;background:var(--brand-blue);font-size:12px}
  .fence{left:34px;top:563px;width:339px;height:27px;background:var(--band-grey);display:flex;align-items:center;justify-content:center;gap:4px;font-size:12px;color:var(--muted)}
  .fence b{color:var(--orange);font-weight:700}
  .fence__arrow{width:16px;height:16px}
  .pillars-lead{left:0;top:594px;width:406px;text-align:center;font-size:10.5px;line-height:12.5px}

  /* pillars */
  .pillars{left:34px;top:625px;width:339px;height:236px;background:var(--deep-blue)}
  .pillars__title{position:absolute;left:0;top:10px;width:339px;text-align:center;color:var(--white);font-size:8px}
  .pillars__dots{position:absolute;left:158px;top:22px;display:flex;gap:3px}
  .pillars__dots i{width:4px;height:4px;border-radius:50%;background:var(--white)}
  .card{position:absolute;width:111px;height:72px;background:var(--white);padding:7px 8px}
  .card h3{font-size:5.5px;color:var(--brand-blue);font-weight:700;display:flex;align-items:center;gap:5px;margin-bottom:7px}
  .card h3::before{content:"";width:6px;height:6px;border-radius:50%;border:1.5px solid #c8361c}
  .card p{font-size:4.2px;line-height:6px;color:#555;padding-left:10px}
  .card--a{left:53px;top:33px}
  .card--b{left:172px;top:33px}
  .card--c{left:53px;top:115px}
  .card--d{left:172px;top:115px}
  .btn--orange{position:absolute;left:23px;top:200px;width:287px;height:28px;line-height:28px;background:var(--orange);font-size:12px}

  /* contact */
  .contact{left:0;top:884px;width:406px;text-align:center;font-size:8.5px;line-height:11px}
  .contact b{font-weight:700;font-size:7.5px}
  .form{left:102px;top:913px;width:198px}
  .field{position:absolute;height:15px;border:1px solid var(--line-grey);font-size:4.5px;color:#aaa;padding:4px 3px;background:var(--white)}
  .field--name{left:0;top:0;width:96px}
  .field--email{left:98px;top:0;width:100px}
  .field--phone{left:0;top:17px;width:198px}
  .field--msg{left:0;top:34px;width:198px;height:58px}

  .divider{left:0;top:1009px;width:406px;height:10px;background:var(--band-grey)}

  /* footer */
  .footer-col{top:1031px;width:64px}
  .footer-col h4{font-size:6px;font-weight:700;margin-bottom:3px}
  .footer-col ul{list-style:none}
  .footer-col li{font-size:4.3px;line-height:6px;color:#333}
  .footer-col--1{left:25px}
  .footer-col--2{left:91px}
  .footer-col--3{left:158px}
  .footer-col--4{left:225px;width:160px}
  .map{position:absolute;left:0;top:11px;width:156px;height:82px;background:linear-gradient(135deg,#d9d6c8,#e6e2d3 60%,#c9d3c3);border:1px solid #9a9a9a}
  .copyright{left:0;top:1145px;width:406px;text-align:center;font-size:4.5px;color:#555}
</style>
</head>
<body>
<main class="page">
  <div class="brand"><span class="brand__name">Vital Summit</span><span class="brand__dot"></span></div>
  <div class="contact-lines"><div><span>Office</span>: 5550142290</div><div><span>Fax</span>: 5550142291</div></div>

  <nav class="nav">
    <a class="is-active" href="#">Home</a>
    <a href="#" style="left:246px">About</a>
    <a href="#" style="left:297px">Service</a>
    <a href="#" style="left:354px">Contact</a>
  </nav>

  <section class="hero">
    <div class="hero__photo" role="img" aria-label="Portrait of Dr. Korwell in a white coat, arms crossed, in a bright clinic corridor"></div>
    <div class="hero__title">
      <h1>Get Side BY Side Support</h1>
      <p>from Dr. Korwell</p>
      <p>Total Wellness Coaching Program</p>
    </div>
    <div class="hero__dots"><i></i><i></i></div>
    <div class="hero__name">Dr. Korwell</div>
  </section>

  <h2 class="headline">Concierge Total Wellnes From a Practicing MD!</h2>
  <p class="intro">Why wait for to doctor appointment when you can receive one on one care on an ongoing basis. Dr. Korwell currently has a four-month wait list to see him in his practice.</p>
  <div class="video" role="img" aria-label="Video still of Dr. Korwell speaking to camera">
    <svg class="video__play" width="24" height="24" viewBox="0 0 24 24"><circle cx="12" cy="12" r="11" fill="#ffffff" fill-opacity="0.55"/><path d="M9.5 7.5 L17 12 L9.5 16.5 Z" fill="#ffffff"/></svg>
  </div>

  <div class="brand brand--center"><span class="brand__name">Vital<br>Summit</span><span class="brand__dot"></span></div>
  <h2 class="commit">Make a Commitment to Yourself</h2>
  <ul class="goals">
    <li>Lost Weight</li><li>Increase Energy</li>
    <li>Conquer Mental Illness</li><li>Live Joyfully</li>
    <li>Build A Better Tribe</li><li>Cultivate Relationship</li>
    <li>Combat Stress &amp; Disease</li><li>Clarify Your Purpose</li>
  </ul>

  <a class="btn btn--blue" href="#">Sign Me Up for Side by Side Coaching with Dr. Korwell</a>
  <div class="fence">Still on the fence? <b>Learn More</b>
    <svg class="fence__arrow" viewBox="0 0 16 16"><circle cx="8" cy="8" r="8" fill="#ef8a1f"/><path d="M8 3.5 V11 M4.8 8 L8 11.5 L11.2 8" stroke="#fff" stroke-width="2" fill="none"/></svg>
  </div>
  <p class="pillars-lead">Dr. Korwell Coaches You Side by Side in areas based on his<br>Five Pillar Formula for Total Wellnes.</p>

  <section class="pillars">
    <div class="pillars__title">About Us</div>
    <div class="pillars__dots"><i></i><i></i><i></i></div>
    <article class="card card--a"><h3>Nutrition</h3><p>Fuel your body in the right ways. With the latest tools and research findings, learn how to change your body on a cellular level for a better life and true vitality.</p></article>
    <article class="card card--b"><h3>Movement</h3><p>Combat daily stressors and degenerative disease through the transformation of exercise. Learn the principles of movement and find out how to increase mobility at any age.</p></article>
    <article class="card card--c"><h3>Tribe</h3><p>Gain perspective on the unique healing power of having a tribe. Learn practices that will assist you in becoming more conscious of who is in your tribe.</p></article>
    <article class="card card--d"><h3>Mindfulness</h3><p>Take a deep dive into individual mindfulness practices that will help you reduce stress, overcome anxiety, conquer disease and increase overall wellbeing.</p></article>
    <a class="btn btn--orange" href="#">Sign Me Up! I am Ready for Change</a>
  </section>

  <div class="contact">Contact<br><b>hello@vitalsummit.com</b></div>
  <form class="form">
    <div class="field field--name">Your Name</div>
    <div class="field field--email">Your Email</div>
    <div class="field field--phone">Phone Number</div>
    <div class="field field--msg">Message</div>
  </form>

  <div class="divider"></div>

  <div class="footer-col footer-col--1"><h4>HOMEOWNERS</h4><ul><li>House Painting</li><li>Exterior Painting</li><li>Interior Painting</li><li>Free Estimates</li><li>Customer FAQs</li><li>Reviews</li><li>Gallery</li><li>Safety</li><li>Window Cleaning</li></ul></div>
  <div class="footer-col footer-col--2"><h4>STUDENTS</h4><ul><li>Programs</li><li>Summer Jobs</li><li>Be an Entrepreneur</li><li>Info for Parents</li><li>Careers</li><li>Culture</li><li>Alumni</li><li>Student FAQs</li></ul></div>
  <div class="footer-col footer-col--3"><h4>ABOUT US</h4><ul><li>Our Promise</li><li>Our History</li><li>Our Locations</li><li>House Painting</li><li>Window Cleaning</li><li>Partnerships</li><li>In the News</li><li>Our Parent Company</li><li>Our People</li></ul></div>
  <div class="footer-col footer-col--4"><h4>LOCATIONS</h4><div class="map" role="img" aria-label="Street map showing the office location"></div></div>

  <p class="copyright">©2024 Vital Summit. All Rights Reserved.</p>
</main>
</body>
</html>
```